Wren Hollow Oils - Body Oils

I am in need of 4 different label and package designs for a new line of body oils that I am launching. I already have the logo and names, it is now a matter of positioning the content. The names are as follows;

1) CARDAMOM + CYPRESS
WARMING BODY OIL
2) NEROLI + LEMON
UPLIFTING BODY OIL
3) CEDAR + BIRCH
GROUNDING BODY OIL
4) SAGE + MINT
COOLING BODY OIL.
The size of each label is 13cm wide x 9.5cm high. The size of the box is 4.5cm x 4.5cm x 15.5cm high.
The size of the bottle is 4cm across the base and 10.5cm in glass height.
I have included an image from a line that I started to work on but it didn't go anywhere. I thought the borders looked good to frame it in however, I am not attached to anything at this point. I am also including a picture of a product line that has used different colors on the packaging. I am not certain that this is the direction I'd like to take however I like how it looks with them. If we were to add the color I think it should be JUST the boxes and NOT the labels and they would be as follows; WARMING OIL - warm burgundy, earth tones UPLIFTING OIL - warm light, lightish blues GROUNDING OIL - warm soft, brownish creams COOLING OIL - refreshing light, pale green possibly blue. I would be interested to see what adding a sprig of a plant would look like on the boxes however with the already busy logo it might look like too much is going on. As you will see in our instagram and website we currently have the bear logo in a foil. I am not sure that I want to proceed with this foil as it is difficult to photograph. I would like to look at colors that compliment the existing line of essential oils as well as the dark brown wood on the cap.
I have added a design that looks a bit industrial that I like, it reads black ops.

Target Market(s)

My market is mainly females who are interested in natural health age 17 - 70. There is a large movement for organic + green beauty. I would like the label to look and feel clean and natural. Something that has been wildcrafted, raw and completely from nature.

Industry/Entity Type

Health And Wellness

Colors

Designer to choose colors to be used in the design.

Requirements
Must have
• Appeal to very progressive organic consumers. Please see the pictures marked SAMPLES 1, 2, 3 + 4 for design ideas.
• Easy to read. Clean design.
• The following information should be on the label as well as the packaging box.
• Size - 100 ML
• Barcodes - still to come
• Ingredients:
• 1) CARDAMOM + CYPRESS WARMING BODY OIL - *Sunflower Oil, **Orange, **Cardamom, **Cypress, **Ginger *Organic, **Organic essential oil
• 2) NEROLI + LEMON UPLIFTING BODY OIL - *Sunflower oil, **Orange, **Neroli, **Grapefruit, **Lemon, **Bergamot, **Benzoin, *Organic, **Organic essential oil
• 3) CEDAR + BIRCH GROUNDING BODY OIL - *Sunflower Oil, **Cedarwood, **Birch, **Benzoin, **Patchouli,*Organic, **Organic essential oil
• 4) SAGE + MINT COOLING BODY OIL - *Sunflower oil, **Spearmint, **Clary Sage, **Geranium, **Ylang Ylang, *Organic, **Organic essential oil
• Suggested Use:
• Warm oil if desired. Apply to the full body after bathing, massage in motions toward the heart until the oil is mostly absorbed. Can also be added to bath water.
Nice to have
• I would like to see the designs on the actual bottle (pic included) to see how it looks.
Should not have
• Bright colors.

```html
<!DOCTYPE html>
<html lang="en">
<head>
<meta charset="utf-8">
<title>Wren Hollow Oils – Cardamom + Cypress Warming Body Oil Label</title>
<link rel="stylesheet" href="https://fonts.googleapis.com/css2?family=Oswald:wght@500;600&family=Open+Sans:wght@400;600&display=swap">
<style>
  :root {
    --page-bg: #ebe8e4;
    --label-bg: #ffffff;
    --band-brown: #6b2c24;
    --ink-brown: #6a3a30;
    --accent-orange: #e2592b;
    --text-on-band: #f4ece8;
    --body-text: #4a3a35;
  }
  html, body {
    margin: 0;
    padding: 0;
    width: 703px;
    height: 1200px;
    overflow: hidden;
    background: var(--page-bg);
  }
  .canvas {
    position: relative;
    width: 703px;
    height: 1200px;
  }
  .label {
    position: absolute;
    left: 22px;
    top: 359px;
    width: 660px;
    height: 482px;
    background: var(--label-bg);
    box-shadow: 0 2px 10px rgba(0,0,0,0.12);
    overflow: hidden;
  }
  .band {
    position: absolute;
    left: 0;
    width: 100%;
    height: 30px;
    background: var(--band-brown);
    color: var(--text-on-band);
    font-family: "Open Sans", sans-serif;
  }
  .band-top { top: 0; }
  .band-bottom { bottom: 0; }
  .band-text {
    position: absolute;
    left: 20px;
    width: 300px;
    text-align: center;
    line-height: 30px;
  }
  .band-top .band-text { font-size: 12px; letter-spacing: 0.3px; }
  .band-bottom .band-text { font-size: 15px; }

  .front-panel {
    position: absolute;
    left: 20px;
    top: 30px;
    width: 300px;
    height: 422px;
  }
  .brand-mark {
    position: absolute;
    top: 40px;
    left: 0;
    width: 100%;
    display: flex;
    flex-direction: column;
    align-items: center;
    gap: 14px;
  }
  .brand-mark .dot {
    width: 38px;
    height: 38px;
    border-radius: 50%;
    background: var(--ink-brown);
  }
  .brand-mark .name {
    font-family: "Oswald", sans-serif;
    font-weight: 500;
    font-size: 24px;
    letter-spacing: 3px;
    color: var(--ink-brown);
  }
  .product-name {
    position: absolute;
    top: 178px;
    left: 0;
    width: 100%;
    text-align: center;
    font-family: "Oswald", sans-serif;
    font-weight: 600;
    color: var(--ink-brown);
    line-height: 1;
    margin: 0;
  }
  .product-name .line-one {
    display: block;
    font-size: 34px;
    letter-spacing: 1px;
  }
  .product-name .line-two {
    display: block;
    font-size: 56px;
    letter-spacing: 1.5px;
    margin-top: 4px;
  }
  .oil-type {
    position: absolute;
    top: 338px;
    left: 65px;
    width: 170px;
    height: 48px;
    background: var(--band-brown);
    text-align: center;
    font-family: "Open Sans", sans-serif;
    font-size: 15px;
    line-height: 1.1;
    display: flex;
    flex-direction: column;
    justify-content: center;
  }
  .oil-type .mood { color: var(--accent-orange); letter-spacing: 1px; }
  .oil-type .kind { color: var(--text-on-band); letter-spacing: 1px; }

  .info-panel {
    position: absolute;
    left: 350px;
    top: 60px;
    width: 270px;
    font-family: "Open Sans", sans-serif;
    font-size: 12.5px;
    line-height: 1.5;
    color: var(--body-text);
  }
  .info-panel h2 {
    font-size: 12.5px;
    font-weight: 600;
    margin: 0 0 2px;
    color: var(--ink-brown);
  }
  .info-panel p { margin: 0 0 18px; }
</style>
</head>
<body>
<div class="canvas">
  <div class="label">
    <div class="band band-top"><span class="band-text">Wren Hollow Oils</span></div>

    <div class="front-panel">
      <div class="brand-mark">
        <span class="dot"></span>
        <span class="name">WREN HOLLOW</span>
      </div>
      <h1 class="product-name">
        <span class="line-one">CARDAMOM +</span>
        <span class="line-two">CYPRESS</span>
      </h1>
      <div class="oil-type">
        <span class="mood">WARMING</span>
        <span class="kind">BODY OIL</span>
      </div>
    </div>

    <div class="info-panel">
      <h2>Ingredients:</h2>
      <p>*Sunflower Oil, **Orange, **Cardamom, **Cypress, **Ginger<br>*Organic **Organic essential oil</p>
      <h2>Suggested Use:</h2>
      <p>Warm oil if desired. Apply to the full body after bathing, massage in motions toward the heart until the oil is mostly absorbed. Can also be added to bath water.</p>
    </div>

    <div class="band band-bottom"><span class="band-text">100ml</span></div>
  </div>
</div>
</body>
</html>
```